Vitamin B12 Liquid Drops Label

hi, i need a label designed for my vitamin b12 drops that i am going to be selling on bazaroo. the label needs to quickly capture the attention of a buyer as he or she is scrolling through the thumbnail search results on bazaroo.example my brand is called zulpa. i already have an example brand logo i will be using, however, i need help designing the rest of the label. attached are some examples of labels i like for other supplements.some of these examples are pink. i do not want pink. please go for a blue/green color scheme. THE DESIGN MUST BE BOLD

Target Market(s)

adults ages 30 - 64

Font styles to use
Sans Serif

Colors
0455a3
cedeed
3176b5
85acd3
cfdeed
9bcb3b
abd037
cadf82
00a990

Requirements
Must have
• - bold design
• - somewhat gender-neutral color scheme because this will be used equally by men and women
• - B12 MUST be very prominent and visible on the label
Should not have
• - it should not be "crunchy" looking

```html
<!DOCTYPE html>
<html lang="en">
<head>
<meta charset="utf-8">
<title>Zulpa B12 Vitamin Drops Label</title>
<link rel="stylesheet" href="https://fonts.googleapis.com/css2?family=Montserrat:wght@300;500&display=swap">
<style>
  :root {
    --backdrop: #9adcd9;
    --panel-light: #cfdeed;
    --panel-light-deep: #bcd0e3;
    --teal: #2aa58c;
    --teal-deep: #1f9680;
    --navy: #2b2363;
    --ink-white: #e6eef5;
    --brand-white: #ffffff;
  }
  * { margin: 0; padding: 0; box-sizing: border-box; }
  html, body {
    width: 1200px;
    height: 1141px;
    overflow: hidden;
    background: var(--backdrop);
  }
  .canvas {
    position: relative;
    width: 1200px;
    height: 1141px;
  }
  .label {
    position: absolute;
    left: 250px;
    top: 70px;
    width: 700px;
    height: 1000px;
    display: flex;
    overflow: hidden;
  }
  .brand-strip {
    position: relative;
    width: 200px;
    height: 100%;
    background: linear-gradient(180deg, var(--panel-light) 0%, var(--panel-light-deep) 100%);
    overflow: hidden;
  }
  .brand-name {
    position: absolute;
    left: -22px;
    bottom: 20px;
    writing-mode: vertical-rl;
    transform: rotate(180deg);
    font-family: "Montserrat", sans-serif;
    font-weight: 300;
    font-size: 250px;
    line-height: 1;
    letter-spacing: 4px;
    color: var(--brand-white);
    white-space: nowrap;
  }
  .product-panel {
    position: relative;
    flex: 1;
    height: 100%;
    background: linear-gradient(180deg, var(--teal) 0%, var(--teal-deep) 100%);
    overflow: hidden;
  }
  .vitamin-code {
    position: absolute;
    left: 34px;
    top: 40px;
    font-family: "Montserrat", sans-serif;
    font-weight: 500;
    font-size: 230px;
    line-height: 1;
    letter-spacing: -4px;
    color: var(--navy);
    white-space: nowrap;
  }
  .product-type {
    position: absolute;
    left: 36px;
    top: 370px;
    font-family: "Montserrat", sans-serif;
    font-weight: 300;
    font-size: 80px;
    line-height: 1.15;
    color: var(--ink-white);
    white-space: nowrap;
  }
</style>
</head>
<body>
  <main class="canvas">
    <section class="label" aria-label="Zulpa B12 Vitamin Drops label">
      <div class="brand-strip">
        <span class="brand-name">ZULPA</span>
      </div>
      <div class="product-panel">
        <h1 class="vitamin-code">B12</h1>
        <p class="product-type">VITAMIN<br>DROPS</p>
      </div>
    </section>
  </main>
</body>
</html>
```